Engineering Consultant Business Card

I'm starting a new business as a high-end engineering consultant in a niche field. I've attached the jpg for my logo plus the branding guideline document that I've been following. You can see my business website here: www.tarvikworks.com
I'd like a business card that has the logo on one side, then the other side has (in any order): Tarvik Works, Inc.
Dana Whitlock
President and Chief EMC Engineer
www.tarvikworks.com
dana@tarvikworks.com
Optional: motto "We will solve your EMC problems as early as possible—ideally before they even start."
I'm not planning on including a phone number
Target Market(s)
Businesses, especially makers of electronics hardware
Industry/Entity Type
Electrical engineering
Contact Information for Business Card
Company name, my name, website, email

```html
<!DOCTYPE html>
<html lang="en">
<head>
<meta charset="utf-8">
<title>Tarvik Works, Inc. – Business Card</title>
<link href="https://fonts.googleapis.com/css2?family=Arimo:wght@400;700&display=swap" rel="stylesheet">
<style>
  :root {
    --backdrop: #d9dadc;
    --card: #000000;
    --ink: #ffffff;
    --accent: #29a9e0;
  }
  * { margin: 0; padding: 0; box-sizing: border-box; }
  html, body {
    width: 1200px;
    height: 675px;
    overflow: hidden;
    background: var(--backdrop);
    font-family: "Arimo", Arial, sans-serif;
    color: var(--ink);
  }
  .sheet {
    width: 1200px;
    height: 675px;
    display: flex;
    align-items: center;
    justify-content: center;
    gap: 40px;
  }
  .card {
    position: relative;
    width: 520px;
    height: 298px;
    background: var(--card);
  }

  /* Front side */
  .card--front {
    display: flex;
    align-items: center;
    justify-content: center;
    gap: 16px;
  }
  .brand-dot {
    width: 54px;
    height: 54px;
    border: 6px solid var(--ink);
    border-radius: 50%;
  }
  .brand-name {
    font-weight: 700;
    font-size: 44px;
    letter-spacing: 0.5px;
  }

  /* Back side */
  .company {
    position: absolute;
    left: 70px;
    top: 58px;
    display: flex;
    align-items: center;
    gap: 12px;
  }
  .company__dot {
    width: 40px;
    height: 40px;
    border: 3px solid var(--ink);
    border-radius: 50%;
  }
  .company__name {
    font-weight: 700;
    font-size: 32px;
  }
  .person {
    position: absolute;
    left: 150px;
    top: 118px;
  }
  .person__name {
    font-weight: 700;
    font-size: 27px;
    line-height: 1.15;
  }
  .person__title {
    font-weight: 400;
    font-size: 17px;
    margin-top: 4px;
  }
  .contact {
    position: absolute;
    top: 226px;
    display: flex;
    align-items: center;
    gap: 10px;
    font-weight: 700;
    font-size: 17px;
  }
  .contact--web { left: 44px; }
  .contact--mail { left: 282px; }
  .contact__icon { width: 24px; height: 24px; flex: none; }
</style>
</head>
<body>
<main class="sheet">
  <section class="card card--front" aria-label="Card front">
    <span class="brand-dot" aria-hidden="true"></span>
    <span class="brand-name">Tarvik Works</span>
  </section>

  <section class="card card--back" aria-label="Card back">
    <div class="company">
      <span class="company__dot" aria-hidden="true"></span>
      <span class="company__name">Tarvik Works, Inc.</span>
    </div>
    <div class="person">
      <p class="person__name">Dana Whitlock</p>
      <p class="person__title">President and Chief EMC Engineer</p>
    </div>
    <p class="contact contact--web">
      <svg class="contact__icon" viewBox="0 0 24 24" aria-hidden="true" fill="none" stroke="var(--accent)" stroke-width="1.6">
        <circle cx="12" cy="12" r="10.5"/>
        <circle cx="12" cy="12" r="6"/>
        <ellipse cx="12" cy="12" rx="2.6" ry="6"/>
        <line x1="6" y1="12" x2="18" y2="12"/>
      </svg>
      www.tarvikworks.com
    </p>
    <p class="contact contact--mail">
      <svg class="contact__icon" viewBox="0 0 24 24" aria-hidden="true" fill="none" stroke="var(--accent)" stroke-width="1.6">
        <circle cx="12" cy="12" r="10.5"/>
        <rect x="6.5" y="8" width="11" height="8" fill="var(--accent)" stroke="none"/>
        <polyline points="6.5,8 12,12.5 17.5,8" stroke="var(--card)" stroke-width="1.2"/>
      </svg>
      dana@tarvikworks.com
    </p>
  </section>
</main>
</body>
</html>
```